"VeltaMakings" Graphic Design Project

We are a new business creating bath/ body/beauty products. We need label designs for men "Plume for Men " and women- "Plume for Women" . Since the collection called Plume will be used for both- we'd like the labels to look similar but separating the gender look- maybe by a same color variation. Our bottles are amber in color , so we like the beiges, cream, and earthy warm tones - greens- brown-orange- yellow-colors. The labels are for 8 oz amber cosmo round bottles. The height is 7.32inches and the diameter is 1.85 inches.
Our starting line will be Plume for Men ( Silk Body Wash, Silk Body Lotion and Body Mist) and the same for Plume for Women.

Target Market(s)

Our target audience is between 30 to 60 years of age. Salons and private consumers.
I am including attached sample of what was started by me.

Industry/Entity Type

Business

Requirements
Must have
• We would like to incorporate the company name- VeltaMakings along with the name of the product- which will be Plume for Men or Plume for Women on each label.

On label with company name or somewhere on label we would like a tree to symbolize the beginning, but we are open to suggestions.

```html
<!DOCTYPE html>
<html lang="en">
<head>
<meta charset="utf-8">
<title>Plume for Men – Silk Body Wash Label</title>
<link href="https://fonts.googleapis.com/css2?family=Quicksand:wght@300;400&display=swap" rel="stylesheet">
<style>
  :root {
    --teal-top: #1c9c92;
    --teal-mid: #16675f;
    --teal-deep: #1b3a38;
    --charcoal: #232727;
    --brand-glow: #2cc0b3;
    --text-light: #f1f5f4;
    --text-soft: #dfeae8;
    --panel-fill: rgba(255, 255, 255, 0.17);
    --bubble: rgba(60, 200, 188, 0.35);
    --spine-edge: rgba(0, 0, 0, 0.35);
    --spine-shine: rgba(255, 255, 255, 0.08);
  }
  html, body {
    margin: 0;
    padding: 0;
    width: 955px;
    height: 1200px;
    overflow: hidden;
    background: var(--charcoal);
  }
  .label {
    position: relative;
    width: 955px;
    height: 1200px;
    overflow: hidden;
    font-family: "Quicksand", sans-serif;
    color: var(--text-light);
    background: linear-gradient(180deg, var(--teal-top) 0%, var(--teal-mid) 40%, var(--teal-deep) 72%, var(--charcoal) 100%);
  }
  .bubbles {
    position: absolute;
    inset: 0;
  }
  .spine {
    position: absolute;
    left: 324px;
    top: 0;
    width: 99px;
    height: 1200px;
    background: linear-gradient(90deg, var(--spine-edge) 0%, var(--spine-shine) 12%, transparent 30%, transparent 72%, var(--spine-shine) 88%, var(--spine-edge) 100%);
  }
  .brand-vertical {
    position: absolute;
    left: 373px;
    top: 604px;
    transform: translate(-50%, -50%) rotate(-90deg);
    font-size: 75px;
    font-weight: 300;
    letter-spacing: 1px;
    color: #e4e6e6;
    white-space: nowrap;
  }
  .front {
    position: absolute;
    left: 0;
    width: 324px;
    text-align: center;
  }
  .product-name {
    top: 136px;
    font-size: 62px;
    font-weight: 400;
    color: var(--brand-glow);
    text-shadow: 0 0 10px rgba(80, 230, 215, 0.45);
  }
  .audience {
    top: 220px;
    font-size: 25px;
    font-weight: 400;
  }
  .product-type {
    top: 608px;
    font-size: 32px;
    font-weight: 400;
  }
  .origin {
    top: 1108px;
    font-size: 22px;
    line-height: 36px;
    font-weight: 400;
  }
  .info {
    position: absolute;
    left: 433px;
    width: 530px;
    text-align: center;
    font-size: 22px;
    line-height: 32px;
    font-weight: 400;
    margin: 0;
  }
  .info.intro { top: 88px; }
  .info.directions { top: 217px; }
  .info.warnings { top: 317px; }
  .info.claim { top: 414px; }
  .ingredients {
    position: absolute;
    left: 442px;
    top: 556px;
    width: 483px;
    height: 416px;
    box-sizing: border-box;
    padding: 32px 14px 0;
    border-radius: 18px;
    background: var(--panel-fill);
    text-align: center;
    font-size: 18px;
    line-height: 26.8px;
    color: var(--text-soft);
  }
  .ingredients p { margin: 0; }
  .company {
    position: absolute;
    left: 433px;
    width: 530px;
    top: 1056px;
    text-align: center;
    font-size: 24px;
    line-height: 33px;
    color: var(--text-soft);
  }
  .company p { margin: 0; }
</style>
</head>
<body>
<main class="label">
  <svg class="bubbles" width="955" height="1200" viewBox="0 0 955 1200" aria-hidden="true">
    <circle cx="70" cy="285" r="75" fill="var(--bubble)"/>
    <circle cx="5" cy="295" r="22" fill="var(--bubble)"/>
    <circle cx="243" cy="307" r="23" fill="var(--bubble)"/>
    <circle cx="232" cy="417" r="22" fill="var(--bubble)"/>
    <circle cx="282" cy="488" r="80" fill="rgba(60,200,188,0.22)"/>
    <circle cx="170" cy="735" r="72" fill="rgba(60,200,188,0.18)"/>
    <circle cx="160" cy="683" r="18" fill="var(--bubble)"/>
    <circle cx="260" cy="880" r="60" fill="rgba(60,200,188,0.12)"/>
    <circle cx="545" cy="505" r="82" fill="rgba(60,200,188,0.25)"/>
    <circle cx="870" cy="255" r="80" fill="rgba(60,200,188,0.28)"/>
    <circle cx="755" cy="1003" r="50" fill="rgba(60,200,188,0.12)"/>
  </svg>

  <div class="spine"></div>
  <div class="brand-vertical">VeltaMakings</div>

  <div class="front product-name">Plume</div>
  <div class="front audience">FOR MEN</div>
  <div class="front product-type">Silk Body Wash</div>
  <div class="front origin">MADE IN USA<br>8.25 fl oz. / 244mL</div>

  <p class="info intro">Our Nourishing Silk Body Wash will engulf you<br>in luxurious lather as it gently cleanses your<br>delicate skin leaving it soft as silk.</p>
  <p class="info directions">Directions: Apply to skin while damp with<br>sponge or wash cloth. Rinse well.</p>
  <p class="info warnings">WARNINGS/CAUTIONS: For external use only.<br>Avoid contact with eyes.</p>
  <p class="info claim">NOT TESTED ON ANIMALS</p>

  <section class="ingredients">
    <p>INGREDIENTS: purified water, sodium olefin<br>sulfonate (plant source), organic aloe barbadensis<br>leaf juice, cocamidopropyl betaine (plant source),<br>sodium chloride (salt), kosher vegetable glycerin,<br>tocopherol (natural vitamin E), polysorbate 20<br>(plant source), potassium sorbate (plant source),<br>phenoxyethanol (mild preservative), caprylyl glycol<br>(plant source), organic anthemis nobilis (chamo-<br>mile) extract, organic calendula officinalis flower<br>extract, xanthan gum (plant source), magnesium<br>ascorbyl phosphate (vitamin C ester), sodium<br>bicarbonate (baking soda), citric acid fragrance.</p>
  </section>

  <footer class="company">
    <p>Veltamakings</p>
    <p>Bath – Body - Home</p>
    <p>Coral Bay, FL&nbsp; 33100</p>
    <p>Shop 24/7 - www.veltamakings.com</p>
  </footer>
</main>
</body>
</html>
```